TORVA tuition homepage (After school courses)

We would like to introduce our tuition rates on new homepage. our website is www.torvanachhilfe.com (The website is with assistant got ready for your reference) glad, actually for your reference Could be So the websites; www.kolbarium.de and www.fennhaus.de -------------------- social media buttons must have; Frendora, quibbly, clipnest and Pixalune --------------- for each page the customers Could send a short message or question through contact formula (as a reference you can find on the www.kolbarium. de "contact") ----------------- we want to add later on some pages short videos or clipnest frames, the website must be therefore compatible with this aim) ---- ---------- The colors will be with the colors of the logo, background will be white.

Target Market(s)

Parents and students 10-18 jähre old

Industry/Entity Type

School

Coding

Coded - Design and coding required

Number of Pages Required

5+ page

Font styles to use
Sans Serif

Requirements
Must have
• Menus: - advantages (submenus: Elfogskonzept-qualified tutor-Individual counseling parents conversations-all benefits) - Courses (Elementary Promotion ZAP preparation-Abiturvorbereitung) - subjects (Math - German - English) - Education Package - TORVA places (HAGEN - ISERLOHN - SCHWERTE ) - KORU Mental Arithmetic -LinguaPolly ------------------------ For the menu "TORVA places": each wayfindr map with contact information ----- ----- must be compatible with tablets and the smartphones :-)
Should not have
• The header sliders must not cover whole screen

```html
<!DOCTYPE html>
<html lang="de">
<head>
<meta charset="utf-8">
<title>TORVA nachhilfe – Alle Vorteile</title>
<link href="https://fonts.googleapis.com/css2?family=Lato:wght@400;700&family=Kalam:wght@400&display=swap" rel="stylesheet">
<style>
:root{
  --brand-blue:#35a6db;
  --dropdown-blue:#2a87ad;
  --text-grey:#5a5a5a;
  --heading-grey:#555;
  --line-grey:#d6d6d6;
  --accent-red:#e94b5a;
  --white:#ffffff;
  --photo-green:#6f8f4a;
  --photo-dark:#3b4a3a;
}
*{margin:0;padding:0;box-sizing:border-box}
html,body{width:1200px;height:938px;overflow:hidden;background:var(--white)}
body{font-family:'Lato',sans-serif;color:var(--text-grey);position:relative}
.site-header{position:absolute;left:0;top:0;width:1200px;height:136px}
.brand{position:absolute;left:0;width:1200px;top:26px;text-align:center}
.brand-mark{display:inline-block;width:44px;height:44px;background:var(--brand-blue)}
.brand-name{display:block;font-size:27px;font-weight:400;color:var(--heading-grey);letter-spacing:.5px;margin-top:2px;line-height:30px}
.brand-tag{display:block;font-size:8.5px;letter-spacing:7px;color:var(--heading-grey);margin-top:0}
.brand-url{display:block;font-size:5.5px;letter-spacing:2px;color:#888}
.main-nav{position:absolute;left:0;top:136px;width:1200px;height:37px;background:var(--brand-blue)}
.main-nav a{position:absolute;top:10px;color:var(--white);font-size:14px;text-decoration:none}
.dropdown{position:absolute;left:185px;top:173px;width:192px;height:144px;background:var(--dropdown-blue);padding-top:14px;z-index:2}
.dropdown a{display:block;color:var(--white);font-size:13.5px;text-decoration:none;padding-left:15px;height:25px}
.hero{position:absolute;left:0;top:173px;width:1200px;height:336px;background:linear-gradient(180deg,#9ab883 0%,var(--photo-green) 45%,var(--photo-dark) 100%)}
.hero-dots{position:absolute;left:552px;top:482px;display:flex;gap:6px}
.hero-dots span{width:11px;height:11px;border-radius:50%;background:var(--white)}
.hero-dots .active{border:3px solid var(--white);background:var(--accent-red)}
.breadcrumb{position:absolute;left:37px;top:524px;font-size:13.5px;color:var(--text-grey)}
.divider{position:absolute;left:0;top:546px;width:1200px;height:2px;background:var(--line-grey)}
.page-title{position:absolute;left:37px;top:572px;font-size:34px;font-weight:400;color:var(--brand-blue)}
.section-title{position:absolute;left:37px;top:636px;font-size:20.5px;font-weight:700;color:var(--heading-grey)}
.intro{position:absolute;left:37px;top:677px;width:570px;font-size:13.4px;line-height:16px;color:var(--text-grey)}
.more-link{position:absolute;left:483px;top:789px;font-family:'Kalam',cursive;font-size:21px;color:var(--accent-red);text-decoration:none;border-bottom:1.5px solid var(--accent-red);line-height:26px}
.feature-image{position:absolute;left:732px;top:581px;width:430px;height:287px;background:radial-gradient(circle at 55% 40%,#e6c23a 0%,#6fbf5a 35%,#7c8d99 75%,#4d5f72 100%)}
</style>
</head>
<body>
<header class="site-header">
  <div class="brand">
    <span class="brand-mark"></span>
    <span class="brand-name">torva nachhilfe</span>
    <span class="brand-tag">PRIVATE TUITION</span>
    <span class="brand-url">www.torvanachhilfe.de</span>
  </div>
</header>
<nav class="main-nav">
  <a href="#" style="left:200px">Vorteile</a>
  <a href="#" style="left:292px">Kurse</a>
  <a href="#" style="left:368px">Fächer</a>
  <a href="#" style="left:450px">Bildungspaket</a>
  <a href="#" style="left:578px">TORVA Orte</a>
  <a href="#" style="left:703px">KORU Mental Arithmetic</a>
  <a href="#" style="left:909px">LinguaPolly</a>
</nav>
<div class="hero" role="img" aria-label="Students sitting together on a sunny lawn studying from books"></div>
<div class="dropdown">
  <a href="#">Elfogskonzept</a>
  <a href="#">Qualifizierte Nachhilfelehrer</a>
  <a href="#">Individuelle Beratung</a>
  <a href="#">Elterngespräche</a>
  <a href="#">Alle Vorteile</a>
</div>
<div class="hero-dots"><span></span><span class="active"></span><span></span><span></span><span></span><span></span></div>
<div class="breadcrumb">Vorteile &gt; Alle Vorteile</div>
<div class="divider"></div>
<h1 class="page-title">Alle Vorteile</h1>
<h2 class="section-title">Unser Erfolgskonzept – Zufriedenheit und Lernfortschritt</h2>
<p class="intro">Erfahrung zahlt sich aus! Seit über 40 Jahren hilft die Kolbarium Kindern und Jugendlichen erfolgreich bei schulischen Problemen. Unser breit gefächertes Nachhilfe- und Förder-Angebot sowie unsere qualifizierten Nachhilfelehrer werden Ihrem Kind zu besseren Noten und mehr Selbstbewusstsein verhelfen! Mit gestärktem Selbstbewusstsein und guten Noten kann Ihr Kind in eine sichere Zukunft starten.</p>
<a class="more-link" href="#">Mehr &gt;</a>
<div class="feature-image" role="img" aria-label="Open hands releasing colourful flying books"></div>
</body>
</html>
```